American pesto sauce company needs a vintage/ old fashioned package design

Company name: Marisol Grove.
We need a food label design for 4 different flavors of pesto sauce: classic almond, sundried tomato, roasted red pepper, and Cajun spice. For those that do not know what pesto is, it is a sauce like tomato sauce that is traditionally Italian and goes on pasta or whatever you choose to put it on and the consistent ingredients are garlic, cheese, nuts, olive oil and basil. They are fresh, all natural without preservatives, artificial flavors or colors.
The design of the jar is an old fashioned wire bale jar used for preserving foods ( attached is a picture). I'm looking for a label with:
• an upscale vintage feel but will also stand out on a grocery store shelf. I have attached an example of the feel I am looking for as well as the format of the words with my company name.
• The word "Pesto" must be prominent on the label.
• metalic gold boarders that go around the whole label maybe with gold embellishments if you see fit for that upscale feeling.
• Also, as you can see in the attachment, there are different typesets. And it must be easy to read from at least 3 feet away.
• Each label will have a different color corresponding to the flavor- could be part of the flavor text
• The bottom of the front panel must have “Net Wt. 5.75 oz (162g)” in a creative format how you see fit. Measures: height-28 mm, width-75mm
• Need logo for top part of label with the letters MG for Marisol Grove and it will also contain the website, address and parent company name, use by date, etc. Measures:50 mm diameter
• The back panel of the label will contain the nutrition facts, ingredients and bar code. Measures: height-28 mm, width-75mm

Also the label is one piece with 3 different sections. Attached will be an example with measurements.
Updates

Check out this website on packaging. I absolutely love love love the Hartwell Pantry almond water labels. The colors for the different flavors. How its not just horizontal or vertical. The different typesets/fonts/typography. The flourishes and background thats faded.
http://brightwrapgallery.com/page/3/

Target Market(s)

Target market is medium- high income foodies between 35-65

Industry/Entity Type

Grocery Store

Requirements
Must have
• Net Wt on front lower panel. Separation of the company name Marisol & Pesto. See attachment.
Nice to have
• Name of flavor designed in a wave pattern as shown in attachment. Hand drawn font OK.

```html
<!DOCTYPE html>
<html lang="en">
<head>
<meta charset="utf-8">
<title>Marisol Grove — Brand and Jar Label</title>
<link rel="stylesheet" href="https://fonts.googleapis.com/css2?family=Josefin+Slab:wght@400;600&family=Oswald:wght@500&family=Arvo:wght@700&family=Roboto+Condensed:ital,wght@1,700&display=swap">
<style>
  :root {
    --paper: #ffffff;
    --ink: #222222;
    --label-black: #1f1f1f;
    --frame-red: #c0342b;
    --cream: #ffffff;
    --gold: #c9a24a;
    --muted: #8a8a8a;
  }
  * { margin: 0; padding: 0; box-sizing: border-box; }
  html, body { width: 1200px; height: 1000px; overflow: hidden; background: var(--paper); }
  .canvas { position: relative; width: 1200px; height: 1000px; }

  .wordmark {
    position: absolute; left: 240px; top: 362px; width: 244px;
    text-align: center; font-family: "Josefin Slab", serif; font-weight: 400;
    color: var(--ink); font-size: 38px; letter-spacing: 9px; line-height: 48px;
  }

  .seal { position: absolute; left: 709px; top: 200px; width: 264px; height: 264px; }
  .seal-name {
    position: absolute; left: 0; top: 0; width: 264px; height: 264px;
    display: flex; align-items: center; justify-content: center; text-align: center;
    font-family: "Josefin Slab", serif; font-weight: 400; color: var(--cream);
    font-size: 26px; letter-spacing: 5px; line-height: 34px;
  }

  .label { position: absolute; left: 164px; top: 573px; width: 873px; height: 326px; background: var(--label-black); }
  .label-frame { position: absolute; left: 12px; top: 12px; width: 849px; height: 302px; border: 4px solid var(--frame-red); }
  .label-lines { position: absolute; left: 0; top: 0; }

  .brand-line {
    position: absolute; left: 172px; top: 46px;
    font-family: "Oswald", sans-serif; font-weight: 500; font-size: 42px; letter-spacing: 2px;
    color: var(--cream); text-shadow: 3px 3px 0 var(--gold); transform: rotate(-2deg);
  }
  .flavor {
    position: absolute; left: 146px; top: 80px;
    font-family: "Oswald", sans-serif; font-weight: 500; font-size: 76px; letter-spacing: 2px;
    color: var(--cream); text-shadow: -5px 5px 0 #6d6d6d; transform: rotate(-2deg); white-space: nowrap;
  }
  .tagline {
    position: absolute; left: 438px; top: 184px; width: 268px;
    display: flex; align-items: center; gap: 10px;
    font-family: "Josefin Slab", serif; font-weight: 600; font-size: 17px; letter-spacing: 4px; color: var(--cream);
  }
  .tagline::before, .tagline::after { content: ""; flex: 1; height: 1px; background: var(--muted); }
  .product {
    position: absolute; left: 436px; top: 208px;
    font-family: "Arvo", serif; font-weight: 700; font-size: 62px; letter-spacing: 5px;
    color: var(--cream); text-shadow: 5px 5px 0 var(--gold);
  }
  .net-weight {
    position: absolute; left: 778px; top: 268px;
    font-family: "Roboto Condensed", sans-serif; font-style: italic; font-weight: 700; font-size: 19px; color: var(--cream);
  }
  .flourish { position: absolute; background: #3a3a3a; border-radius: 14px; }
</style>
</head>
<body>
<main class="canvas">

  <div class="wordmark">MARISOL<br>-GROVE-</div>

  <div class="seal">
    <svg width="264" height="264" viewBox="0 0 264 264" aria-hidden="true">
      <circle cx="132" cy="132" r="131" fill="var(--label-black)"/>
      <circle cx="132" cy="132" r="120" fill="none" stroke="var(--frame-red)" stroke-width="3"/>
    </svg>
    <div class="seal-name">MARISOL<br>GROVE</div>
  </div>

  <section class="label">
    <div class="label-frame"></div>
    <svg class="label-lines" width="873" height="326" viewBox="0 0 873 326" aria-hidden="true">
      <path d="M364 76 Q500 62 644 58" stroke="var(--cream)" stroke-width="4" fill="none" stroke-linecap="round"/>
      <path d="M120 240 Q260 226 372 222" stroke="var(--cream)" stroke-width="4" fill="none" stroke-linecap="round"/>
    </svg>
    <div class="brand-line">MARISOL</div>
    <div class="flavor">CAJUN PEPPER</div>
    <div class="tagline">ALL NATURAL</div>
    <div class="product">PESTO</div>
    <div class="net-weight">575oz</div>
    <div class="flourish" role="img" aria-label="Small scroll flourish beside the flavor name" style="left:652px;top:128px;width:52px;height:40px;"></div>
    <div class="flourish" role="img" aria-label="Small scroll flourish with curl above the left rule" style="left:268px;top:218px;width:138px;height:54px;"></div>
  </section>

</main>
</body>
</html>
```